Business card - house cleaning company

We want friendly high end business card highlighting our services . NO LOGOs on back of card please.. no vertical cards NO DOUBLE BROOMS

2 owners of the company: Corinne Halvey & Joel Brandt

Included phone number: (555)318-2047

Email: brightlanetidy@mailnest.example

Website: www.brightlanetidy.example

Bonded & Insured

Pinecrest Falls, CO 80599

Slogan maybe: Bringing a brighter shine to every corner of home

We want elegant high end card for house cleaning service. Maybe 2 sided if needed. Can it have bullet points of some services we offer

Residential Home Cleaning
Vacation Rental Cleaning
Commercial Cleaning
Carpet Cleaning
Window Cleaning
Property Management
Property Inspections
Property Maintenance
Trash Removal
Concierge Services

Highlight service on back of card. If we can do a one sided card with all this that’s great as well. Not cartoony.

Our logo attached and a design somone I had Perrin but they put very little time in. Not Unique enough. If you can do a custom design with a feminine touch that be great.

You will be eliminated for not reading the brief. NO DOUBLE LOGOS NO DOUBLE BROOMS. PLEASE BE CREATIVE. IF POST SAME LOGO WITH SMAL CHANGES RHEY WILL BE ELIMINATED. BE CREATIVE.

Thank you everyone for your designs. please only use the logo 1 time. and would love to see some that dont look all the same. We appreciate your time.

Target Market(s)

Residential and vacation rental home cleaning maid service

Industry/Entity Type

House cleaning maid services

Contact Information for Business Card

For business card use logo. black and green one provided. others for example. I wil try find some example.. We want friendly high end look. 2 owners of the company: Corinne Halvey & Joel Brandt Included phone number: (555)318-2047 Email: brightlanetidy@mailnest.example Website: www.brightlanetidy.example Bonded & Insured Estes Park, CO Slogan maybe: Bringing a brighter shine to every corner of home or Quality Service Guaranteed We want elegant high end card for house cleaning service. Maybe 2 sided if needed. Can it have bullet points of some services we offer Residential Home Cleaning Vacation Rental Cleaning Commercial Cleaning Carpet Cleaning Window Cleaning Property Management Property Inspections Property Maintenance Trash Removal Concierge Services

Requirements
Must have
• For business card use logo . Creativity. black and green one provided. We want friendly high end look. 2 owners of the company: Corinne Halvey & Joel Brandt Included phone number: (555)318-2047 Email: brightlanetidy@mailnest.example Website: www.brightlanetidy.example Licensed Bonded & Insured Estes Park, CO Slogan maybe: Bringing a brighter shine to every corner of home or Quality Service Guaranteed We want elegant high end card for house cleaning service. Maybe 2 sided if needed. Can it have bullet points of some services we offer Residential Home Cleaning Vacation Rental Cleaning Commercial Cleaning Carpet Cleaning Window Cleaning Property Management Property Inspections Property Maintenance Trash Removal Concierge Services .. creatitivty a plus. whimsical. we like stars..
Nice to have
• we want much better than the example of biz card provided as example. logo has colors that are in our website palette as well. We are open to ideas for the business card design. Will pay tip to best work. PLEASE USE COMPLIMENTING COLORS. . WE LIKE BLACK AND WHITE, stars
Should not have
• NO DOUBLE LOGOS. READ READ. READ. YOU WILL BE ELIMINATED no double logos or double brooms same side of card. I want didfrent examples. please don't make all your submission look the same

```html
<!DOCTYPE html>
<html lang="en">
<head>
<meta charset="utf-8">
<title>Brightlane Tidy – Business Card</title>
<link href="https://fonts.googleapis.com/css2?family=Playfair+Display:wght@500&family=Poppins:wght@300;400;500;600&display=swap" rel="stylesheet">
<style>
  :root {
    --bg: #eeebea;
    --card: #ffffff;
    --blue: #2f6690;
    --green: #6f9a3f;
    --white: #ffffff;
    --mist-green: #e6e9dc;
    --mist-blue: #dde2ea;
  }
  * { margin: 0; padding: 0; box-sizing: border-box; }
  html, body { width: 1200px; height: 1200px; overflow: hidden; }
  body { background: var(--bg); font-family: "Poppins", sans-serif; position: relative; }

  .card { position: absolute; width: 775px; height: 442px; overflow: hidden; box-shadow: 0 14px 26px rgba(0,0,0,0.14); }
  .card-front { left: 176px; top: 138px; background: var(--card); }
  .card-back { left: 181px; top: 633px; background: var(--blue); }

  /* Front */
  .accent-bar { position: absolute; top: 65px; height: 64px; background: var(--green); }
  .accent-bar.left { left: 0; width: 26px; }
  .accent-bar.right { left: 746px; width: 29px; }

  .name-band { position: absolute; left: 32px; top: 65px; width: 424px; height: 64px; background: var(--blue); color: var(--white); padding: 4px 0 0 24px; }
  .owner-names { font-family: "Playfair Display", serif; font-weight: 500; font-size: 26px; line-height: 32px; white-space: nowrap; }
  .owner-title { font-weight: 300; font-size: 17px; line-height: 20px; }

  .brand-name { position: absolute; left: 478px; top: 74px; width: 256px; height: 46px; font-weight: 600; font-size: 29px; line-height: 46px; color: var(--blue); display: flex; align-items: center; justify-content: center; gap: 10px; white-space: nowrap; }
  .brand-dot { width: 14px; height: 14px; border-radius: 50%; background: var(--green); flex: none; }

  .credential { position: absolute; left: 32px; top: 181px; font-weight: 500; font-size: 21px; color: var(--green); letter-spacing: 0.3px; }
  .credential-rule { position: absolute; left: 32px; top: 212px; width: 38px; height: 2px; background: var(--blue); }

  .contact-list { position: absolute; left: 32px; top: 245px; list-style: none; }
  .contact-item { display: flex; align-items: center; height: 28px; font-size: 20px; color: var(--blue); white-space: nowrap; }
  .contact-item.location { margin-top: 21px; }
  .contact-icon { width: 18px; height: 18px; margin-right: 12px; flex: none; }
  .web-accent { color: var(--green); }

  .mountain-glow { position: absolute; left: 362px; top: 271px; width: 413px; height: 171px; background: radial-gradient(ellipse at 60% 70%, var(--mist-green) 0%, rgba(230,233,220,0.5) 45%, rgba(255,255,255,0) 75%); }

  /* Back */
  .services-title { position: absolute; left: 0; width: 735px; top: 104px; text-align: center; font-weight: 500; font-size: 42px; line-height: 52px; color: var(--white); }
  .services-rule { position: absolute; left: 177px; top: 170px; width: 398px; height: 2px; background: var(--white); border-radius: 1px; }
  .service-list { position: absolute; top: 209px; list-style: none; }
  .service-list.col-one { left: 31px; }
  .service-list.col-two { left: 430px; }
  .service-item { display: flex; align-items: center; height: 35.6px; font-size: 22px; color: var(--white); white-space: nowrap; }
  .service-bullet { width: 9px; height: 9px; border-radius: 50%; background: var(--white); margin: 0 31px 0 10px; flex: none; }
  .col-two .service-bullet { margin-right: 36px; }
</style>
</head>
<body>

<section class="card card-front" aria-label="Business card front">
  <div class="accent-bar left"></div>
  <div class="name-band">
    <p class="owner-names">Corinne Halvey &amp; Joel Brandt</p>
    <p class="owner-title">owner</p>
  </div>
  <div class="brand-name"><span class="brand-dot"></span>Brightlane Tidy</div>
  <div class="accent-bar right"></div>

  <p class="credential">Bonded &amp; Insured</p>
  <div class="credential-rule"></div>

  <div class="mountain-glow" role="img" aria-label="Faint mountain range with sparkling stars"></div>

  <ul class="contact-list">
    <li class="contact-item">
      <svg class="contact-icon" viewBox="0 0 24 24"><path fill="#6f9a3f" d="M6.6 10.8a15.1 15.1 0 0 0 6.6 6.6l2.2-2.2a1 1 0 0 1 1-.25 11.4 11.4 0 0 0 3.6.57 1 1 0 0 1 1 1V20a1 1 0 0 1-1 1A17 17 0 0 1 3 4a1 1 0 0 1 1-1h3.5a1 1 0 0 1 1 1c0 1.25.2 2.45.57 3.57a1 1 0 0 1-.25 1z"/></svg>
      (555)318-2047
    </li>
    <li class="contact-item">
      <svg class="contact-icon" viewBox="0 0 24 24"><rect x="2" y="5" width="20" height="14" fill="#6f9a3f"/><path d="M2 5l10 8 10-8" fill="none" stroke="#fff" stroke-width="1.6"/></svg>
      brightlanetidy@mailnest.example
    </li>
    <li class="contact-item">
      <svg class="contact-icon" viewBox="0 0 24 24"><circle cx="12" cy="12" r="10" fill="#6f9a3f"/><path d="M2 12h20M12 2c3 3 3 17 0 20M12 2c-3 3-3 17 0 20" fill="none" stroke="#fff" stroke-width="1.4"/></svg>
      <span>www.<span class="web-accent">brightlanetidy</span>.example</span>
    </li>
    <li class="contact-item location">
      <svg class="contact-icon" viewBox="0 0 24 24"><path fill="#6f9a3f" d="M12 1a8 8 0 0 0-8 8c0 6 8 14 8 14s8-8 8-14a8 8 0 0 0-8-8zm0 11a3 3 0 1 1 0-6 3 3 0 0 1 0 6z"/></svg>
      Pinecrest Falls, CO 80599
    </li>
  </ul>
</section>

<section class="card card-back" aria-label="Business card back">
  <h2 class="services-title">Our Services</h2>
  <div class="services-rule"></div>
  <ul class="service-list col-one">
    <li class="service-item"><span class="service-bullet"></span>Residential Home Cleaning</li>
    <li class="service-item"><span class="service-bullet"></span>Vacation Rental Cleaning</li>
    <li class="service-item"><span class="service-bullet"></span>Commercial Cleaning</li>
    <li class="service-item"><span class="service-bullet"></span>Carpet Cleaning</li>
    <li class="service-item"><span class="service-bullet"></span>Window Cleaning</li>
  </ul>
  <ul class="service-list col-two">
    <li class="service-item"><span class="service-bullet"></span>Property Management</li>
    <li class="service-item"><span class="service-bullet"></span>Property Inspections</li>
    <li class="service-item"><span class="service-bullet"></span>Property Maintenance</li>
    <li class="service-item"><span class="service-bullet"></span>Trash Removal</li>
    <li class="service-item"><span class="service-bullet"></span>Concierge Services</li>
  </ul>
</section>

</body>
</html>
```